Solar Panel Leaflet Advert Design

Looking for an advertising leaflet A5
I want something that stands out and will encourage those who see it to call and not the throw the leaflet in the bin.

I want the picture of an install as the back ground

See pic of previous leaflet i had made a few years back
Im looking for something along those lines

To say
6.66kw System designed and installed for $4500
18 x 370w Velmar Solar Panels
1 x Catrel Nuvo 5kW Inverter

if possible without over crowding i want:
Installed by Local In House Team - No Sub contractors
Support Small Family Business
Check our Facebook for Pictures and Reviews

Please include license numbers at bottom as per old leaflet
same subject to as old leaflet, but please add 'subject to site inspection'

```html
<!DOCTYPE html>
<html lang="en">
<head>
<meta charset="utf-8">
<title>Solar System Leaflet</title>
<link rel="stylesheet" href="https://fonts.googleapis.com/css2?family=Bebas+Neue&family=Montserrat:wght@500;700;800&display=swap">
<style>
  :root{
    --red:#d42027;
    --red-soft:#e0575c;
    --ink:#1f1f1f;
    --bar:#2b2b2b;
    --paper:#ffffff;
    --stage:#f2f2f2;
    --rule:#cfcfcf;
  }
  html,body{margin:0;padding:0;width:1200px;height:2573px;overflow:hidden;background:var(--stage);}
  .leaflet{position:absolute;left:80px;top:548px;width:1040px;height:1477px;background:var(--paper);box-shadow:0 10px 30px rgba(0,0,0,.18);}
  .leaflet svg{display:block;width:1040px;height:1477px;}
  .display{font-family:'Bebas Neue',Impact,sans-serif;}
  .body-text{font-family:'Montserrat',Arial,sans-serif;}
  .ink{fill:var(--ink);}
  .accent{fill:var(--red);}
  .white{fill:#fff;}
</style>
</head>
<body>
<main class="leaflet">
<svg viewBox="0 0 785 1115" xmlns="http://www.w3.org/2000/svg">
  <defs>
    <linearGradient id="roofTones" x1="0" y1="1" x2="1" y2="0">
      <stop offset="0" stop-color="#5a5560"/>
      <stop offset="0.55" stop-color="#3f3b52"/>
      <stop offset="0.8" stop-color="#7a6a66"/>
      <stop offset="1" stop-color="#c8683e"/>
    </linearGradient>
    <linearGradient id="productTones" x1="0" y1="0" x2="1" y2="0">
      <stop offset="0" stop-color="#1a1a1e"/>
      <stop offset="0.55" stop-color="#2a2a30"/>
      <stop offset="0.62" stop-color="#c9c9cc"/>
      <stop offset="1" stop-color="#e6e6e8"/>
    </linearGradient>
  </defs>

  <!-- install photograph background -->
  <path class="install-photo" role="img" aria-label="Aerial photo of a rooftop solar panel installation on a metal roof beside terracotta tiles"
        fill="url(#roofTones)"
        d="M0 225 C180 250 380 205 520 0 L785 0 L785 460 C700 430 640 465 600 500 L440 520 C300 565 150 590 0 560 Z"/>

  <!-- top red sweep -->
  <path class="sweep-top" fill="var(--red)" d="M230 222 C380 200 470 110 500 0 L525 0 C480 130 390 215 230 226 Z"/>
  <path class="sweep-top-soft" fill="var(--red-soft)" d="M300 218 C420 190 490 110 525 0 L540 0 C500 120 430 200 300 222 Z"/>

  <!-- lower red swoosh -->
  <path class="swoosh-main" fill="var(--red)" d="M0 560 C150 600 320 585 440 505 L440 540 C330 625 150 640 0 600 Z"/>
  <path class="swoosh-line" fill="none" stroke="var(--red)" stroke-width="5" stroke-linecap="round" d="M80 650 C210 662 340 640 440 585"/>

  <!-- curve behind products -->
  <path class="swoosh-right" fill="var(--red-soft)" d="M630 425 C700 410 760 430 785 470 L785 495 C750 468 700 458 640 470 Z"/>

  <!-- product photograph -->
  <rect class="product-photo" role="img" aria-label="Product photo of a solar panel and a Catrel Nuvo inverter" x="432" y="295" width="313" height="420" rx="14" fill="url(#productTones)"/>

  <!-- certification mark -->
  <g class="council-mark">
    <circle cx="95" cy="105" r="52" fill="var(--red)"/>
    <text class="body-text accent" x="162" y="80" font-size="30" font-weight="700">SUNWARD</text>
    <text class="body-text accent" x="162" y="115" font-size="30" font-weight="700">ENERGY</text>
    <text class="body-text accent" x="162" y="150" font-size="30" font-weight="700">BOARD</text>
  </g>

  <!-- offer -->
  <g class="offer">
    <text class="display ink" x="38" y="726" font-size="44">6.66KW  SOLAR SYSTEM</text>
    <text class="display accent" x="38" y="780" font-size="58">DESIGNED AND</text>
    <text class="display accent" x="38" y="833" font-size="58">INSTALLED FOR</text>
    <text class="display ink" x="38" y="908" font-size="32">$</text>
    <text class="display ink" x="62" y="912" font-size="82">4500</text>
  </g>

  <!-- inclusions -->
  <g class="inclusions body-text" font-weight="700" font-size="23">
    <g class="tick-box" fill="none" stroke="var(--red)" stroke-width="4" stroke-linecap="round" stroke-linejoin="round">
      <path d="M66 952 H42 V988 H76 V968"/>
      <path d="M50 968 L60 980 L80 952"/>
    </g>
    <text class="ink" x="110" y="962">18 x 370w Velmar</text>
    <text class="ink" x="110" y="993">Solar Panels</text>
    <g class="tick-box" fill="none" stroke="var(--red)" stroke-width="4" stroke-linecap="round" stroke-linejoin="round">
      <path d="M66 1030 H42 V1066 H76 V1046"/>
      <path d="M50 1046 L60 1058 L80 1030"/>
    </g>
    <text class="ink" x="110" y="1040">1 x Catrel Nuvo</text>
    <text class="ink" x="110" y="1071">5kW Inverter</text>
  </g>

  <line class="divider" x1="376" y1="752" x2="376" y2="1000" stroke="var(--rule)" stroke-width="2"/>

  <!-- terms -->
  <g class="terms body-text" text-anchor="end">
    <text class="ink" x="746" y="770" font-size="21" font-weight="800">RESIDENTIAL &amp;</text>
    <text class="ink" x="746" y="798" font-size="21" font-weight="800">COMMERCIAL CUSTOMERS.</text>
    <text class="ink" x="746" y="826" font-size="21" font-weight="800">STANDARD INSTALLATION</text>
    <g font-size="15" font-weight="500" class="ink">
      <text x="746" y="858">Contractors license BLD 318274 CEC</text>
      <text x="746" y="878">license A5521930</text>
      <text x="746" y="898">Subject to eligibility of government</text>
      <text x="746" y="918">solar scheme rebate and assignment</text>
      <text x="746" y="938">of STC's to HALDEN ELECTRICAL.</text>
    </g>
    <text class="display" x="746" y="994" font-size="36"><tspan class="ink">SUBJECT TO </tspan><tspan class="accent">SITE INSPECTION</tspan></text>
  </g>

  <!-- footer -->
  <rect class="footer-bar" x="0" y="1096" width="785" height="19" fill="var(--bar)"/>
  <path class="call-block" fill="var(--red)" d="M398 1013 L785 1013 L785 1115 L350 1115 Z"/>
  <g class="call">
    <circle cx="440" cy="1056" r="20" fill="#fff"/>
    <path fill="var(--red)" d="M431 1044 c2-2 5-1 6 1 l3 6 c1 2 0 4-2 5 l-2 1 c2 4 5 7 9 9 l1-2 c1-2 3-3 5-2 l6 3 c2 1 3 4 1 6 l-3 3 c-4 3-13 0-20-7 c-7-7-10-16-7-20 Z"/>
    <text class="display white" x="488" y="1082" font-size="66">0400 615 283</text>
  </g>
</svg>
</main>
</body>
</html>
```